Talbrin Business Cards

Front and back. Simon Kavelle MBA is the CEO of Talbrin Homes. Black white and grays. Logo and cool design.

Target Market(s)

Professional lenders and investors

Industry/Entity Type

Real estate developer. NO HOUSES OR ROOFS

Contact Information for Business Card

Logo, name and unique design. Front and back. Simon Kavelle MBA is the CEO of Talbrin Homes. Black white and grays. Logo and cool design.

Font styles to use
Sans Serif

Colors

Designer to choose only greyscale colors for use in the design.

Requirements
Must have
• Cool look. Not the same card I could design.
Nice to have
• Something memorable
Should not have
• Basic

```html
<!DOCTYPE html>
<html lang="en">
<head>
<meta charset="utf-8">
<title>Talbrin Homes – Business Cards</title>
<link href="https://fonts.googleapis.com/css2?family=Arimo:wght@400;700&display=swap" rel="stylesheet">
<style>
  :root {
    --stage: #e9e9e9;
    --paper: #fbfbfb;
    --ink: #2b2b2b;
    --ink-soft: #555555;
    --ink-muted: #6a6a6a;
    --white: #ffffff;
  }
  * { box-sizing: border-box; margin: 0; padding: 0; }
  html, body { width: 1200px; height: 802px; overflow: hidden; }
  body {
    background: var(--stage);
    font-family: "Arimo", Arial, sans-serif;
    display: flex;
    align-items: center;
    justify-content: center;
    gap: 60px;
  }
  .card {
    position: relative;
    width: 520px;
    height: 297px;
    box-shadow: 0 6px 18px rgba(0,0,0,0.18);
    overflow: hidden;
  }

  /* Front: information side */
  .card--front { background: var(--paper); }
  .brand-column {
    position: absolute;
    left: 38px;
    top: 0;
    width: 168px;
    height: 100%;
  }
  .brand-column__block {
    position: absolute;
    left: 0;
    width: 100%;
    background: var(--ink);
  }
  .brand-column__block--top { top: 38px; height: 96px; }
  .brand-column__block--bottom { top: 190px; bottom: 0; }
  .brand-column__name {
    position: absolute;
    top: 148px;
    left: 0;
    width: 100%;
    text-align: center;
    font-weight: 700;
    font-size: 25px;
    letter-spacing: -0.5px;
    color: var(--ink);
    white-space: nowrap;
  }

  .contact {
    position: absolute;
    left: 240px;
    top: 58px;
    color: var(--ink-soft);
  }
  .contact__name {
    font-weight: 700;
    font-size: 17px;
    color: var(--ink);
    letter-spacing: 0.3px;
  }
  .contact__title { font-size: 14px; margin-top: 2px; color: var(--ink-muted); }
  .contact__address { font-size: 14px; margin-top: 14px; line-height: 1.35; color: var(--ink-muted); }
  .contact__list { list-style: none; margin-top: 10px; }
  .contact__item {
    display: flex;
    align-items: center;
    gap: 8px;
    font-size: 14px;
    line-height: 1.6;
    color: var(--ink-muted);
  }
  .contact__icon { width: 12px; height: 12px; flex: none; }

  /* Back: brand side */
  .card--back {
    background: var(--ink);
    display: flex;
    align-items: center;
    justify-content: center;
  }
  .card--back .brand-name {
    font-weight: 700;
    font-size: 46px;
    letter-spacing: -1px;
    color: var(--white);
  }
</style>
</head>
<body>

  <section class="card card--front" aria-label="Card front">
    <div class="brand-column">
      <div class="brand-column__block brand-column__block--top"></div>
      <div class="brand-column__name">Talbrin Homes</div>
      <div class="brand-column__block brand-column__block--bottom"></div>
    </div>

    <div class="contact">
      <p class="contact__name">SIMON KAVELLE MBA</p>
      <p class="contact__title">CEO</p>
      <p class="contact__address">Your Address, City<br>State, Zip 0000</p>
      <ul class="contact__list">
        <li class="contact__item">
          <svg class="contact__icon" viewBox="0 0 12 12" aria-hidden="true">
            <circle cx="6" cy="6" r="6" fill="var(--ink)"/>
            <path d="M4 3.2c.3-.3.7-.3.9 0l.5.7c.2.3.1.6-.1.8l-.3.3c.3.6.8 1.1 1.4 1.4l.3-.3c.2-.2.5-.3.8-.1l.7.5c.3.2.3.6 0 .9l-.4.4c-.4.4-1.1.4-1.6.1C5 7.2 4.3 6.5 3.6 5.2c-.3-.5-.2-1.2.1-1.6z" fill="var(--white)"/>
          </svg>
          123-456-2100
        </li>
        <li class="contact__item">
          <svg class="contact__icon" viewBox="0 0 12 12" aria-hidden="true">
            <rect x="0.5" y="2" width="11" height="8" fill="var(--ink)"/>
            <path d="M1 2.5l5 4 5-4" fill="none" stroke="var(--white)" stroke-width="1"/>
          </svg>
          youremail@mailhub.com
        </li>
        <li class="contact__item">
          <svg class="contact__icon" viewBox="0 0 12 12" aria-hidden="true">
            <circle cx="6" cy="6" r="6" fill="var(--ink)"/>
            <circle cx="6" cy="6" r="3" fill="none" stroke="var(--white)" stroke-width="1"/>
            <path d="M3 6h6M6 3v6" stroke="var(--white)" stroke-width="0.8"/>
          </svg>
          www.yourwebsite.com
        </li>
      </ul>
    </div>
  </section>

  <section class="card card--back" aria-label="Card back">
    <p class="brand-name">Talbrin Homes</p>
  </section>

</body>
</html>
```